Modern Brochure Design for Music School !!

I would like to have a brochure (A4 two fold) created for my partners music school. I would like it to incorporate information from his website, showing what classes are taught (singing lessons, drum lessons, guitar lessons and keyboard lessons). I would like to keep the same font style or as close to what's on the website if possible.

It needs to grab attention and be modern in design to attract age group of 18-35 while briefly detailing what services they provide, including their location and phone number

Info can all be found on the website www.themelodyloft.com.au

Target Market(s)

18-35 y/o

Industry/Entity Type

School

Font styles to use
Serif

Colors
000000

Requirements
Must have
• Key content from website
• List of classes (singing, drums, guitar, keyboard)
• Address / phone number
• Find us on Facebook - The Melody Loft /Instagram @the_melody_loft
• Mention - gift vouchers available
• Black and white colours preferably no bright colours (like website)
• Modern and professional please!!
Nice to have
• Same type font as website or close to
• Not too much content
Should not have
• .

```html
<!DOCTYPE html>
<html lang="en">
<head>
<meta charset="utf-8">
<title>The Melody Loft – Brochure</title>
<link href="https://fonts.googleapis.com/css2?family=Dosis:wght@300;400;600&family=Catamaran:wght@400&display=swap" rel="stylesheet">
<style>
  :root{
    --stage:#5f5e5f;
    --ink:#0a0a0a;
    --panel:#3a3a3a;
    --light:#f2f2f2;
    --mid:#9a9a9a;
    --white:#ffffff;
  }
  *{margin:0;padding:0;box-sizing:border-box}
  html,body{width:1200px;height:1200px;overflow:hidden;background:var(--stage)}
  .canvas{position:relative;width:1200px;height:1200px}
  .spread{position:absolute;left:82px;width:1036px;height:519px;overflow:hidden}
  .spread--outer{top:67px}
  .spread--inner{top:614px}
  .spread svg.bg{position:absolute;inset:0}
  .abs{position:absolute}
  .heading{font-family:'Dosis',sans-serif;font-weight:300;color:var(--white);text-transform:uppercase}

  /* outer spread */
  .contacts{left:0;top:323px;width:267px;height:167px;background:var(--panel);padding:30px 0 0 37px;color:var(--white)}
  .contacts h3{font-family:'Dosis',sans-serif;font-weight:600;font-size:13px;margin-bottom:8px;letter-spacing:.2px}
  .contacts li{list-style:none;display:flex;align-items:center;gap:8px;font-family:'Catamaran',sans-serif;font-size:10px;height:18px}
  .contacts svg{flex:none}
  .brand{left:780px;top:40px;width:260px;text-align:center;color:var(--white)}
  .brand__name{font-family:'Dosis',sans-serif;font-weight:600;font-size:30px;letter-spacing:1px;text-transform:uppercase}
  .brand__tag{font-family:'Catamaran',sans-serif;font-size:13px;margin-top:10px;letter-spacing:.5px}
  .url{left:700px;top:475px;width:320px;text-align:center;color:var(--white);font-family:'Catamaran',sans-serif;font-size:15px;letter-spacing:1.4px}

  /* inner spread */
  .mission{left:0;top:45px;width:520px;text-align:center}
  .mission p{font-size:15px;line-height:19px}
  .mission .big{font-size:40px;line-height:44px;margin:2px 0 4px}
  .belief{left:115px;top:368px;width:360px;text-align:center;color:var(--ink);font-family:'Dosis',sans-serif;font-weight:400;font-size:26px;line-height:32px}
  .lessons-title{left:554px;top:34px}
  .lessons-title h2{font-size:32px;line-height:32px}
  .lessons-title span{display:block;font-size:10px;margin-top:2px}
  .col{width:96px;text-align:center;font-family:'Catamaran',sans-serif;font-size:9.5px;line-height:12.4px;color:var(--ink)}
  .available{left:600px;top:436px;width:110px;text-align:center;color:var(--white);font-family:'Dosis',sans-serif;font-size:9.5px;line-height:12px;text-transform:uppercase}
  .available b{font-weight:600}
  .instru{left:830px;top:395px;width:200px;text-align:right}
  .instru .big{font-size:30px;line-height:30px}
  .instru .small{font-size:10px}
  .instru .mental{font-size:36px;line-height:36px}
</style>
</head>
<body>
<div class="canvas">

  <!-- Outer spread: back cover + front cover -->
  <section class="spread spread--outer">
    <svg class="bg" width="1036" height="519" viewBox="0 0 1036 519">
      <defs>
        <linearGradient id="guitarTone" x1="0" y1="0" x2="1" y2="1">
          <stop offset="0" stop-color="#d9d9d9"/>
          <stop offset=".45" stop-color="#6b6b6b"/>
          <stop offset="1" stop-color="#2a2a2a"/>
        </linearGradient>
        <linearGradient id="micTone" x1="0" y1="0" x2="1" y2="1">
          <stop offset="0" stop-color="#2b2b2b"/>
          <stop offset=".5" stop-color="#9b9b9b"/>
          <stop offset="1" stop-color="#1c1c1c"/>
        </linearGradient>
      </defs>
      <rect x="0" y="0" width="518" height="519" fill="url(#guitarTone)" role="img" aria-label="Photo of a guitarist playing an acoustic guitar"/>
      <rect x="518" y="0" width="518" height="519" fill="var(--ink)"/>
      <polygon points="518,89 756,89 708,387 518,387" fill="url(#guitarTone)" role="img" aria-label="Continuation of the guitar neck photo"/>
      <polygon points="768,149 1036,149 1036,449 722,449" fill="url(#micTone)" role="img" aria-label="Photo of a studio condenser microphone"/>
      <line x1="802" y1="0" x2="732" y2="455" stroke="#cfcfcf" stroke-width="1.2"/>
      <line x1="720" y1="470" x2="710" y2="519" stroke="#cfcfcf" stroke-width="1.2"/>
    </svg>

    <div class="contacts abs">
      <h3>BUSINESS CONTACTS:</h3>
      <ul>
        <li><svg width="12" height="12" viewBox="0 0 12 12"><circle cx="6" cy="6" r="6" fill="#fff"/><path d="M6 2.5a2 2 0 0 0-2 2c0 1.5 2 4 2 4s2-2.5 2-4a2 2 0 0 0-2-2z" fill="#3a3a3a"/></svg>112 Ellery Road Northvale Victoria</li>
        <li><svg width="12" height="12" viewBox="0 0 12 12"><circle cx="6" cy="6" r="6" fill="#fff"/><path d="M4 3.2l1 1.3-.5.8a4 4 0 0 0 2.2 2.2l.8-.5 1.3 1-.6 1c-2.6-.3-4.6-2.3-5-5z" fill="#3a3a3a"/></svg>1300 555 017</li>
        <li><svg width="12" height="12" viewBox="0 0 12 12"><circle cx="6" cy="6" r="6" fill="#fff"/><path d="M3.5 3.5L9 6 3.5 8.5l.8-2.5z" fill="#3a3a3a"/></svg>info@themelodyloft.com.au</li>
        <li><svg width="12" height="12" viewBox="0 0 12 12"><circle cx="6" cy="6" r="6" fill="#fff"/></svg>The Melody Loft</li>
        <li><svg width="12" height="12" viewBox="0 0 12 12"><circle cx="6" cy="6" r="6" fill="#fff"/></svg>@the_melody_loft</li>
      </ul>
    </div>

    <div class="brand abs">
      <div class="brand__name">The Melody Loft</div>
      <div class="brand__tag">Be Prepared! Be Professional!</div>
    </div>
    <div class="url abs">www.themelodyloft.com.au</div>
  </section>

  <!-- Inner spread -->
  <section class="spread spread--inner">
    <svg class="bg" width="1036" height="519" viewBox="0 0 1036 519">
      <defs>
        <linearGradient id="crowdTone" x1="0" y1="0" x2="0" y2="1">
          <stop offset="0" stop-color="#3c3a3b"/>
          <stop offset=".5" stop-color="#8d8b8c"/>
          <stop offset="1" stop-color="#141414"/>
        </linearGradient>
        <linearGradient id="drumTone" x1="0" y1="0" x2="1" y2="1">
          <stop offset="0" stop-color="#4a4a4a"/>
          <stop offset=".5" stop-color="#222"/>
          <stop offset="1" stop-color="#0c0c0c"/>
        </linearGradient>
        <linearGradient id="stripe" x1="0" y1="0" x2="1" y2="0">
          <stop offset="0" stop-color="#d4d4d4"/>
          <stop offset=".5" stop-color="#f7f7f7"/>
          <stop offset="1" stop-color="#d4d4d4"/>
        </linearGradient>
        <clipPath id="band">
          <polygon points="0,430 926,0 1036,0 1036,166 358,519 0,519"/>
        </clipPath>
      </defs>
      <rect x="0" y="0" width="518" height="519" fill="url(#crowdTone)" role="img" aria-label="Photo of a concert crowd silhouetted against stage lights"/>
      <rect x="518" y="0" width="518" height="519" fill="url(#drumTone)" role="img" aria-label="Photo of a performer with raised hand and a drum kit"/>
      <g clip-path="url(#band)">
        <rect x="0" y="0" width="518" height="519" fill="#f1f1f1"/>
        <rect x="518" y="0" width="104" height="519" fill="url(#stripe)"/>
        <rect x="622" y="0" width="104" height="519" fill="url(#stripe)"/>
        <rect x="726" y="0" width="104" height="519" fill="url(#stripe)"/>
        <rect x="830" y="0" width="104" height="519" fill="url(#stripe)"/>
        <rect x="934" y="0" width="102" height="519" fill="url(#stripe)"/>
      </g>
    </svg>

    <div class="mission heading abs">
      <p>We strive to make the world a nicer place to be in,</p>
      <p class="big">One voice at a time</p>
      <p>Fun and affordable one-on-one vocal tuition</p>
      <p>and now guitar, drums and keyboard tuition</p>
      <p style="margin-top:6px">All ages – all levels of experience – all modern vocal styles</p>
      <p style="margin-top:6px">Brand new location 112 Ellery Road</p>
      <p>Northvale, Victoria</p>
    </div>

    <div class="belief abs">WE BELIEVE THAT<br>ANYONE CAN LEARN<br>HOW TO SING</div>

    <div class="lessons-title heading abs">
      <h2>Lessons</h2>
      <span>Start something like this..</span>
    </div>

    <div class="col abs" style="left:522px;top:210px">Lessons with The Melody Loft generally last for 30 minutes, involve one-on-one tuition and are available Monday through Saturday , between the hours of 12pm and 9pm. Saturdays 10am through to 3pm</div>
    <div class="col abs" style="left:626px;top:154px">If you require an alternative arrangement, such as group lessons at your home or coaching in the studio while you record that all important demo or EP, we will gladly accommodate such arrangements wherever possible.</div>
    <div class="col abs" style="left:730px;top:102px">Lessons with Owen, our Principal Instructor, Monday to Thursday . Lessons with Mia, Tuesdays and Fridays . Jake, is the newest member to The Melody Loft team, teaches Guitar on Monday's. Vocals Monday, Wednesdays and Saturdays.</div>
    <div class="col abs" style="left:834px;top:98px">Discount rates apply where 10 lessons are paid for in advance, or where a student refers a family member or friend to us.</div>
    <div class="col abs" style="left:936px;top:14px">We ask that you bring a USB storage device to each lesson, to which we can save your assigned vocal exercises for practicing at home. If you do not have access to a computer at home, we can put your vocal exercises on a CD instead.</div>

    <div class="available abs">Lessons are available now!<br><b>Keyboard lessons<br>Guitar lessons<br>Teaching is our passion</b></div>

    <div class="instru heading abs">
      <div class="big">The Melody Loft</div>
      <div class="small">Has gone</div>
      <div><span class="small">Instru</span><span class="mental">Mental</span></div>
    </div>
  </section>

</div>
</body>
</html>
```